Real Estate Business Cards

Looking for a clean, sharp and professional look for our Real Estate investment Fund that invests in Multi Family Apartment buildings.

Target Market(s)

Real Estate Fund

Industry/Entity Type

Real Estate

Contact Information for Business Card

Company Description: Real Estate Investment Fund
Company Name: RKW Holdings
Name: Marcus Olvane
Cell: (917) 482-0657
Email: marcus@rkwholdings-example.com
Website: www.rkwholdings-example.com
Address: 418, 9th Street, Brooklyn NY 11218

Colors

Designer to choose colors to be used in the design.

Requirements
Nice to have
• Colors to match logo

```html
<!DOCTYPE html>
<html lang="en">
<head>
<meta charset="utf-8">
<title>RKW Holdings – Business Cards</title>
<link rel="stylesheet" href="https://fonts.googleapis.com/css2?family=Cinzel:wght@400&family=Montserrat:wght@400;500&display=swap">
<style>
  :root {
    --backdrop: #1c1f24;
    --card: #3d3e40;
    --card-edge: #2e2f31;
    --brand-blue: #1565b3;
    --ink-light: #e9e9e9;
    --ink-soft: #cfcfcf;
    --white: #ffffff;
  }
  * { margin: 0; padding: 0; box-sizing: border-box; }
  html, body {
    width: 1200px; height: 900px; overflow: hidden;
    background: var(--backdrop);
  }
  .stage {
    position: relative; width: 1200px; height: 900px;
    display: flex; flex-direction: column; align-items: center; justify-content: center; gap: 48px;
  }
  .card {
    position: relative; width: 588px; height: 336px;
    background: var(--card);
    box-shadow: 0 12px 28px rgba(0,0,0,.45);
    overflow: hidden;
  }

  /* Front */
  .front .brand {
    position: absolute; left: 0; top: 0; width: 286px; height: 100%;
    display: flex; flex-direction: column; align-items: center; justify-content: center; gap: 22px;
  }
  .brand-square {
    width: 46px; height: 46px; background: var(--brand-blue);
  }
  .brand-name {
    font-family: "Cinzel", serif; font-weight: 400;
    font-size: 25px; letter-spacing: 1px; color: var(--white);
  }
  .divider {
    position: absolute; left: 296px; top: 74px; width: 1px; height: 172px;
    background: var(--brand-blue);
  }
  .contact {
    position: absolute; left: 314px; top: 72px; right: 20px;
    font-family: "Montserrat", sans-serif; color: var(--ink-light);
  }
  .contact .person {
    font-family: "Cinzel", serif; font-size: 19px; color: var(--brand-blue);
    letter-spacing: 1px; line-height: 1.1;
  }
  .contact .role { font-size: 14px; margin-top: 4px; }
  .contact .address { font-size: 13.5px; line-height: 1.35; margin-top: 2px; }
  .contact ul { list-style: none; margin-top: 8px; }
  .contact li {
    display: flex; align-items: center; gap: 8px;
    font-size: 12.5px; line-height: 1.7; white-space: nowrap;
  }
  .contact li svg { width: 12px; height: 12px; flex: none; }
  .edge-band {
    position: absolute; left: 0; bottom: 0; width: 100%; height: 7px; display: flex;
  }
  .edge-band .blue { width: 42%; background: var(--brand-blue); }
  .edge-band .white { flex: 1; background: var(--white); }

  /* Back */
  .back .pattern-field {
    position: absolute; inset: 0;
    background: radial-gradient(circle at 50% 45%, #434446 0%, #3a3b3d 70%, #353638 100%);
  }
  .back .brand {
    position: absolute; inset: 0;
    display: flex; flex-direction: column; align-items: center; justify-content: center; gap: 24px;
  }
  .back .brand-square { width: 42px; height: 42px; }
  .back .brand-name { font-size: 23px; }
</style>
</head>
<body>
<main class="stage">

  <section class="card front" aria-label="Business card front">
    <div class="brand">
      <div class="brand-square"></div>
      <div class="brand-name">RKW HOLDINGS</div>
    </div>
    <div class="divider"></div>
    <div class="contact">
      <div class="person">MARCUS OLVANE</div>
      <div class="role">President</div>
      <div class="address">418, 9th Street<br>Brooklyn NY 11218</div>
      <ul>
        <li>
          <svg viewBox="0 0 12 12" aria-hidden="true"><circle cx="6" cy="6" r="5.3" fill="none" stroke="#1565b3" stroke-width="1.2"/><path d="M4.2 3.4l1 .9-.5.8c.4.9 1 1.5 1.9 1.9l.8-.5.9 1-.7.8c-1.9-.3-3.5-1.9-3.8-3.8z" fill="#1565b3"/></svg>
          (917) 482-0657
        </li>
        <li>
          <svg viewBox="0 0 12 12" aria-hidden="true"><rect x=".8" y="2.2" width="10.4" height="7.6" fill="none" stroke="#1565b3" stroke-width="1.2"/><path d="M1 2.6l5 4 5-4" fill="none" stroke="#1565b3" stroke-width="1.2"/></svg>
          marcus@rkwholdings-example.com
        </li>
        <li>
          <svg viewBox="0 0 12 12" aria-hidden="true"><circle cx="6" cy="6" r="5.2" fill="none" stroke="#1565b3" stroke-width="1.2"/><ellipse cx="6" cy="6" rx="2.2" ry="5.2" fill="none" stroke="#1565b3" stroke-width="1"/><path d="M.8 6h10.4" stroke="#1565b3" stroke-width="1"/></svg>
          www.rkwholdings-example.com
        </li>
      </ul>
    </div>
    <div class="edge-band"><span class="blue"></span><span class="white"></span></div>
  </section>

  <section class="card back" aria-label="Business card back">
    <div class="pattern-field" role="img" aria-label="Faint repeating brand pattern across the card back"></div>
    <div class="brand">
      <div class="brand-square"></div>
      <div class="brand-name">RKW HOLDINGS</div>
    </div>
  </section>

</main>
</body>
</html>
```